northbrookeaves.ca vehicle wrap

We need a wrap designed for Trekmaster Van used for sales. We import an innovative gutter system from Sweden then market and distribute across Canada. We want to showcase the versatilty, functionality and asthetics of individual components in a technical theme. View files and instructionsh at https://halvorsenroofline.example-share.com/:f:/s/extranet/QmWxPa7bnd3KzRTcLp9Fh_ZCO4_bmj-vH8yBXlQZ2RtewN?e=KoPLMV
Updates
Went on vacation/holiday
Target Market(s)
Contractors, Architects and builders.
Industry/Entity Type
Construction Company
Colors
Designer to choose colors to be used in the design.
Look and feel
Each slider illustrates characteristics of the customer's brand and the style your logo design should communicate.

```html
<!DOCTYPE html>
<html lang="en">
<head>
<meta charset="utf-8">
<title>northbrookeaves.ca – Trekmaster Van wrap</title>
<link rel="stylesheet" href="https://fonts.googleapis.com/css2?family=Montserrat:wght@600;700&display=swap">
<style>
  :root {
    --wrap-charcoal: #3c3c3e;
    --wrap-orange: #e07a2a;
    --wrap-white: #ffffff;
    --trim-dark: #2a2a2b;
    --glass: #c9cacc;
    --page: #ffffff;
  }
  html, body {
    margin: 0;
    padding: 0;
    overflow: hidden;
    background: var(--page);
  }
  .canvas {
    position: relative;
    width: 1200px;
    height: 569px;
    overflow: hidden;
    background: var(--page);
    font-family: "Montserrat", sans-serif;
  }
  .wrap-art {
    position: absolute;
    inset: 0;
    width: 1200px;
    height: 569px;
  }
  .brand-block {
    position: absolute;
    left: 690px;
    top: 196px;
    width: 410px;
    color: var(--wrap-white);
  }
  .brand-name {
    margin: 0;
    font-weight: 600;
    font-size: 39px;
    line-height: 1;
    letter-spacing: -0.5px;
    color: var(--wrap-white);
  }
  .brand-rule {
    height: 2px;
    margin-top: 6px;
    background: var(--wrap-white);
  }
  .brand-phone {
    margin: 8px 0 0;
    font-weight: 700;
    font-size: 37px;
    line-height: 1;
    letter-spacing: 0.5px;
  }
  .brand-web {
    margin: 9px 0 0 66px;
    font-weight: 700;
    font-size: 16.5px;
    line-height: 1;
    color: var(--wrap-orange);
  }
</style>
</head>
<body>
<div class="canvas">
  <svg class="wrap-art" viewBox="0 0 1200 569" xmlns="http://www.w3.org/2000/svg">
    <defs>
      <clipPath id="van-body">
        <path d="M40 318 Q44 296 70 290 L180 262 Q200 250 215 232 L330 100 Q360 70 410 66 L1110 58 Q1140 58 1148 80 L1156 120 L1158 400 Q1158 418 1140 420 L1012 420 A70 70 0 0 0 876 420 L318 428 A74 74 0 0 0 172 430 L50 430 Q36 428 36 410 Z"/>
      </clipPath>
      <linearGradient id="tone-gutter" x1="0" y1="0" x2="1" y2="1">
        <stop offset="0" stop-color="#b9cde0"/>
        <stop offset="1" stop-color="#6f7377"/>
      </linearGradient>
      <linearGradient id="tone-canopy" x1="0" y1="0" x2="0" y2="1">
        <stop offset="0" stop-color="#9ea9b8"/>
        <stop offset="1" stop-color="#c9a27c"/>
      </linearGradient>
      <linearGradient id="tone-downpipe" x1="0" y1="0" x2="1" y2="0">
        <stop offset="0" stop-color="#8c9094"/>
        <stop offset="1" stop-color="#d9dbdd"/>
      </linearGradient>
    </defs>

    <g class="van-panels" clip-path="url(#van-body)">
      <rect class="panel-orange" x="0" y="0" width="1200" height="569" fill="var(--wrap-orange)"/>
      <polygon class="swoosh-white" points="30,300 380,214 900,60 1200,40 1200,140 30,330" fill="var(--wrap-white)"/>
      <polygon class="panel-charcoal" points="30,322 400,236 660,156 1040,82 1160,128 1200,140 1200,569 30,569" fill="var(--wrap-charcoal)"/>
      <rect class="rocker-orange" x="30" y="398" width="1200" height="26" fill="var(--wrap-orange)"/>
      <rect class="rocker-trim" x="30" y="424" width="1200" height="20" fill="var(--trim-dark)"/>
      <path class="side-glass" d="M236 160 Q240 150 252 150 L374 150 Q386 150 386 162 L386 238 L236 240 Z" fill="var(--glass)"/>
    </g>

    <g class="component-tiles" stroke="var(--wrap-white)" stroke-width="3">
      <circle role="img" aria-label="Photo of a metal half-round gutter on a stone wall" cx="576" cy="188" r="94" fill="url(#tone-gutter)"/>
      <circle role="img" aria-label="Photo of a metal canopy roof at sunset" cx="480" cy="304" r="60" fill="url(#tone-canopy)"/>
      <circle role="img" aria-label="Photo of a round metal downpipe" cx="590" cy="310" r="48" fill="url(#tone-downpipe)"/>
    </g>
  </svg>

  <div class="brand-block">
    <p class="brand-name">northbrookeaves.ca</p>
    <div class="brand-rule"></div>
    <p class="brand-phone">Tel. 604-555-0172</p>
    <p class="brand-web">www.northbrookeaves.ca</p>
  </div>
</div>
</body>
</html>
```